Steady Yield Contract Playbooks for busy people

"Necessity is the mother of invention"

The idea of vetting investment strategies is not new in the financial world before investing real monies. Vetting strategies in options strategies always have been a difficult exercise. Such exercise requires access to programmers, right tools and good historical data. These factors make vetting process very costly and tedious. Becuase of this reason, this process is mostly limited to hedge funds, private banking, wealth management firms. Very few products existed in the market to support this process.

Since my graduation in engineering with major in Computer Science, I worked in large global banks as an IT consultant. Over there, I was designing, developing or managing large IT projects. This job profile demanded long hours, busy and tiring days. Very few hours or literally, not enough time available to analyze investment opportunities.

Moreover, investing in stocks without understanding valuation, business model and financials of the companies often result in losses. More so, if not enough understanding on when to exit from a position. Entering into a position is easy and it is in trader's control but exiting a position when profiting and cutting losses is an important step to make money consistently. This needed more disciplined approach and defined rules for position sizing, money management, profit taking and cutting losses.

Options have greeks that will affect its pricing. Understanding and leading options is another major step in the hurdle of investing in options. There are good mentors/experts teaching options. Gaining conceptual understanding is not that difficult. Practically seeing the market affecting the options trades is the most difficult step. Mentors/experts use primitive tools that give some peek into the practical process but it is very tedious since they often provide manual backtesting. "Options" provide options. There are a lot of questions that need to be answered.

Which options strategy is right?
How to select the expiration date for each options strategy?
How to select the strikes involved in options strategy?
There is an option to paper trade and gain knowledge in these areas. But it is a slow process. To speed things up, I founded Korvane platform which speeds up vetting process. Moreover, all the tests done in the process of strategy design is remembered by the platform. If there a study that can deliver reward expectations for the acceptable risk amount, it can be locked to produce the trading opportunities on any interval. This makes it easy to use model for busy people.

The rest of the book is not to make you experts in all trading areas but it is targeted to help busy people with enough understanding to help you learn, trade carefully knowing that options trading has different risk characteristics. You can refer to them in detail on PWT website. All studies published in this book does not guarantee a future success but they have produced results in the past. These should be taken as educational reference.
Updates

This design is for Print book. Below is about the author. Book needs to have bar code printed and ISBN listed on the back as well. Tomas Brennick, Founder, Korvane Markets Tomas is a computer science engineer with more than two decades of experience working for major financial institutions Vuma, RT Holdings, and PLWN. During his time at Orlundt Advisory Services, he spearheaded a large global delivery team, led business growth in Latin America from the ground up, and was directly responsible for customer experience and software delivery. During this time, he discovered the passion for trading options. Leveraging this against his extensive experience in computer software architecture, Tomas ventured out on his own to found and created www.korvanemarkets.example

Target Market(s)

Busy people with money and want to invest in stock market

Industry/Entity Type

Investment

Font styles to use
Sans Serif

Colors

Designer to choose colors to be used in the design.

Requirements
Must have
• 6 x 9 book. Title of book is "Steady Yield Contract Playbooks" and the subtitle is "for busy people". The author is Tomas Brennick.
• This is soft cover with 155 pages

```html
<!DOCTYPE html>
<html lang="en">
<head>
<meta charset="utf-8">
<title>Steady Yield Contract Playbooks – Cover Spread</title>
<link rel="stylesheet" href="https://fonts.googleapis.com/css2?family=Noto+Serif:wght@500;600;700&family=Libre+Franklin:wght@400;500&display=swap">
<style>
  :root {
    --page-bg: #ffffff;
    --back-dark: #2a2d33;
    --back-mid: #3b4048;
    --spine: #3e4764;
    --front-top: #1c3a5e;
    --front-mid: #2f7fb3;
    --front-glow: #8fd3ef;
    --front-bottom: #0d2a3a;
    --author-band: #1f7d86;
    --text-light: #ffffff;
    --serif: "Noto Serif", Georgia, serif;
    --sans: "Libre Franklin", Arial, sans-serif;
  }
  * { margin: 0; padding: 0; box-sizing: border-box; }
  html, body {
    width: 1200px; height: 1200px; overflow: hidden;
    background: var(--page-bg);
  }
  .spread {
    position: absolute; left: 13px; top: 178px;
    width: 1174px; height: 844px;
    display: flex;
  }
  .back-cover {
    position: relative; width: 563px; height: 100%;
    background: linear-gradient(160deg, var(--back-mid) 0%, var(--back-dark) 45%, #1e2126 100%);
    color: var(--text-light);
  }
  .back-photo {
    position: absolute; inset: 0;
    background: radial-gradient(ellipse at 30% 75%, rgba(120,130,140,0.25), transparent 60%);
  }
  .author-bio {
    position: absolute; left: 23px; top: 36px; width: 520px;
    font-family: var(--serif); font-weight: 600;
    font-size: 21.6px; line-height: 31.3px;
    text-align: justify; letter-spacing: 0.2px;
  }
  .drop-cap {
    font-size: 62px; line-height: 40px; font-weight: 700;
    float: left; margin: 2px 2px 0 0;
  }
  .site-url {
    position: absolute; left: 17px; top: 785px; width: 303px;
    border-top: 1.5px solid rgba(255,255,255,0.85);
    padding-top: 6px;
    font-family: var(--serif); font-weight: 600; font-size: 20.5px;
  }
  .barcode-area {
    position: absolute; left: 353px; top: 716px;
    width: 188px; height: 112px; background: #ffffff;
  }
  .spine {
    width: 48px; height: 100%; background: var(--spine);
    color: var(--text-light);
    display: flex; flex-direction: column; align-items: center;
  }
  .spine-title {
    writing-mode: vertical-rl;
    font-family: var(--serif); font-size: 26px; font-weight: 500;
    margin-top: 22px; white-space: nowrap;
  }
  .spine-author {
    writing-mode: vertical-rl;
    font-family: var(--sans); font-size: 26px;
    margin-top: 56px; white-space: nowrap;
  }
  .front-cover {
    position: relative; width: 563px; height: 100%;
    color: var(--text-light); overflow: hidden;
  }
  .front-photo {
    position: absolute; inset: 0;
    background:
      radial-gradient(ellipse at 55% 60%, rgba(143,211,239,0.75), transparent 45%),
      linear-gradient(180deg, var(--front-top) 0%, var(--front-mid) 50%, #3a9bc8 68%, var(--front-bottom) 100%);
  }
  .book-title {
    position: absolute; left: 0; top: 28px; width: 100%;
    text-align: center;
    font-family: var(--serif); font-weight: 700;
    font-size: 50px; line-height: 70px;
    text-shadow: 0 2px 4px rgba(0,0,0,0.35);
  }
  .book-subtitle {
    position: absolute; left: 0; top: 214px; width: 100%;
    text-align: center;
    font-family: var(--sans); font-weight: 500; font-size: 38px;
  }
  .author-band {
    position: absolute; left: 0; bottom: 0; width: 100%; height: 66px;
    background: var(--author-band);
    display: flex; align-items: center; justify-content: center;
    font-family: var(--sans); font-size: 40px; letter-spacing: 0.5px;
  }
</style>
</head>
<body>
  <div class="spread">
    <section class="back-cover">
      <div class="back-photo" role="img" aria-label="Faint dark photo of stock ticker numbers on a screen"></div>
      <p class="author-bio"><span class="drop-cap">T</span>omas is a computer science engineer with more than two decades of experience working for major financial institutions Vuma, RT Holdings, and PLWN. During his time at Orlundt Advisory Services, he spearheaded a large global delivery team, led business growth in Latin America from the ground up, and was directly responsible for customer experience and software delivery. During this time, he discovered the passion for trading options. Leveraging this against his extensive experience in computer software architecture, Tomas ventured out on his own to found and created Korvane platform.</p>
      <div class="site-url">www.korvanemarkets.example</div>
      <div class="barcode-area"></div>
    </section>

    <section class="spine">
      <div class="spine-title">Steady Yield Contract Playbooks</div>
      <div class="spine-author">Tomas Brennick</div>
    </section>

    <section class="front-cover">
      <div class="front-photo" role="img" aria-label="Blue photo of a world map with market figures over a city skyline and silhouettes of business people shaking hands"></div>
      <h1 class="book-title">Steady Yield<br>Contract Playbooks</h1>
      <p class="book-subtitle">For Busy People</p>
      <div class="author-band">Tomas Brennick</div>
    </section>
  </div>
</body>
</html>
```